Inspection Company - Commercial Brochure Design

We are looking to finalize our 8 x 11 brochure. We are an industry leader in our space of commercial and home inspections.

We really like the front and back design labeled-

We have made some suggestions for the internal pages-

These are only suggestions for the interior section- The wording should remain the same. The images can be removed / rearranged/ etc. There is full creative freedom for the interior.

Wording for Inside Right Page-
With over 500,000 properties inspected we know how to inspect each building type to maximize a Return On Investment for our clients. . Our Inspectors focus on all the critical building components (structural, roof, electrical, plumbing, air and heating, drainage, etc.), health and safety issues – emergency egress and other potential hazards. We document current condition and any immediate and future repairs that are necessary. When scheduling our team take all details into account building construction type, age, location, and property use into consideration to ensure we are fully prepared to conduct a thorough inspection.

Target Market(s)

Investors- Commercial Real Estate Investors

Industry/Entity Type

Commercial Real Estate Inspections

Requirements
Must have
• Similar branding to our website (https://quorvato.com/tamberlycommercial) (https://tamberlyinspections.com/) and ( the uploaded documents (Commercial report cover sample.JPG & plovenrift_z6se15j73jk0fe9fc2samkecn7_image (1).jpg )
Nice to have
• Must have Brand Logos and Brand Colors- Nice to have creative ideas of displaying the information

```html
<!DOCTYPE html>
<html lang="en">
<head>
<meta charset="utf-8">
<title>Tamberly Group – Commercial Brochure Pages</title>
<link rel="stylesheet" href="https://fonts.googleapis.com/css2?family=Roboto:wght@400;500;700&family=Open+Sans:wght@300;400&display=swap">
<style>
  :root{
    --canvas:#d4d4d4;
    --navy-deep:#0f2a48;
    --navy:#1a4a7c;
    --blue:#225f99;
    --panel:#2f6391;
    --panel-dark:#265680;
    --tile-line:#2c6aa6;
    --icon:#2c86d0;
    --white:#ffffff;
    --ink:#1d1d1d;
    --badge-gold:#c9a23a;
    --badge-red:#c8202a;
    --badge-gray:#5b5b5b;
  }
  *{margin:0;padding:0;box-sizing:border-box}
  html,body{width:1200px;height:719px;overflow:hidden;background:var(--canvas)}
  body{position:relative;font-family:"Roboto",Arial,sans-serif}
  .page{position:absolute;top:16px;width:509px;height:655px;background:var(--white);overflow:hidden}
  .page--left{left:27px}
  .page--right{left:666px}
  .band-top{position:absolute;left:0;top:20px;width:100%;height:157px;
    background:linear-gradient(180deg,var(--navy-deep) 0%,var(--navy) 55%,var(--blue) 100%)}
  .band-bottom{position:absolute;left:0;top:503px;width:100%;height:152px;
    background:linear-gradient(180deg,var(--navy-deep) 0%,var(--navy) 55%,var(--blue) 100%)}
  .brand{position:absolute;left:34px;top:34px;display:flex;align-items:center;gap:8px}
  .brand__dot{width:58px;height:58px;border:4px solid var(--white);border-radius:50%}
  .brand__name{color:var(--white);font-weight:700;font-size:15px;letter-spacing:.5px}
  .intro{position:absolute;left:92px;top:86px;width:377px;color:var(--white);
    font-size:10.5px;line-height:11.4px;text-align:justify;text-indent:13px}
  .badge{position:absolute;top:195px;width:76px;height:76px;border-radius:50%}
  .badge--gold{left:53px;background:radial-gradient(circle,#3a5fa0 45%,var(--badge-gold) 47%)}
  .badge--red{left:217px;background:radial-gradient(circle,var(--badge-red) 40%,#fff 42%,#fff 60%,var(--badge-red) 62%)}
  .badge--gray{left:377px;background:radial-gradient(circle,var(--badge-gray) 60%,#8a8a8a 62%)}
  .cred{position:absolute;top:285px;width:118px}
  .cred--a{left:33px}.cred--b{left:195px}.cred--c{left:356px}
  .cred__title{height:30px;background:var(--panel);color:var(--white);font-size:16px;font-weight:500;
    display:flex;align-items:center;justify-content:center}
  .cred__body{margin-top:3px;height:131px;background:var(--panel-dark);color:var(--white);
    font-size:10px;line-height:11.3px;padding:6px 9px}
  .cred__body b{font-weight:700}
  .mark-faint{position:absolute;left:32px;top:498px;width:152px;height:152px;border-radius:50%;
    border:7px solid rgba(255,255,255,.22)}
  .tagline{position:absolute;right:29px;top:531px;text-align:right;color:var(--white);font-size:11px;line-height:12.4px}
  .domain{position:absolute;right:34px;top:617px;color:var(--white);font-family:"Open Sans",Arial,sans-serif;
    font-weight:300;font-size:13px;letter-spacing:1px}
  .title{position:absolute;left:90px;top:95px;color:var(--white);font-size:21px;font-weight:400;letter-spacing:.3px}
  .sky{position:absolute;left:0;top:177px;width:100%;height:326px;
    background:linear-gradient(160deg,#e8edf3 0%,#cdd7e3 45%,#b4c3d4 100%)}
  .grid{position:absolute;left:13px;top:192px;display:grid;grid-template-columns:repeat(3,87px);
    grid-template-rows:63px 63px 63px 63px;column-gap:6px;row-gap:7px}
  .tile{border:1.5px solid var(--tile-line);background:rgba(255,255,255,.35);display:flex;flex-direction:column;
    align-items:center;justify-content:center;gap:6px;font-size:9px;font-weight:700;color:var(--ink)}
  .tile svg{width:24px;height:24px}
  .inspector{position:absolute;left:323px;top:183px;width:147px;height:386px;border-radius:40px 40px 10px 10px;
    background:linear-gradient(180deg,#8b8f97 0%,#3b3f46 40%,#8e939b 70%,#6f7379 100%)}
</style>
</head>
<body>
<svg width="0" height="0" style="position:absolute">
  <symbol id="bldg" viewBox="0 0 24 24"><g fill="none" stroke="#2c86d0" stroke-width="1.6">
    <rect x="3" y="5" width="18" height="16"/><path d="M7 9h2M11 9h2M15 9h2M7 13h2M11 13h2M15 13h2M10 21v-4h4v4"/></g></symbol>
</svg>

<section class="page page--left">
  <div class="band-top"></div>
  <div class="brand"><span class="brand__dot"></span><span class="brand__name">TAMBERLY GROUP</span></div>
  <p class="intro">Our clients appreciate the clear and high quality information that we provide, which helps in negotiations and understanding the overall condition of the commercial property. Commercial real estate is a big investment and its highly advised you make an initial investment in an inspection with a Certified Team of Experts before finalizing a transaction.&nbsp; Trust our team of experts who are Certified with the industries highest accolades.</p>

  <div class="badge badge--gold" role="img" aria-label="Certification badge"></div>
  <div class="badge badge--red" role="img" aria-label="Association badge"></div>
  <div class="badge badge--gray" role="img" aria-label="Realtor association badge"></div>

  <div class="cred cred--a"><div class="cred__title">CCPSB</div>
    <div class="cred__body">Certified Commercial Property Standards Board -Highest degree of training and standards adhering to the International Standards of Practice forInspecting Commercial Properties (ComISP)</div></div>
  <div class="cred cred--b"><div class="cred__title">INTERVERIS</div>
    <div class="cred__body">Worlds largest Certifying body for the inspection industry. Interveris Association of Certified Home Inspectors</div></div>
  <div class="cred cred--c"><div class="cred__title">P.R.A</div>
    <div class="cred__body"><b>Pacific Realty Alliance Certified Inspectors</b> Verified Association Credentials, Background checks, and verified Insurance Documents.</div></div>

  <div class="band-bottom"></div>
  <div class="mark-faint"></div>
  <p class="tagline">ALL THIS TO ENSURE YOUR&nbsp; GETTING<br>THE MOST THOROUGH COMMERCIAL<br>INSPECTION AVAILABLE</p>
  <p class="domain">QUORVATO.COM</p>
</section>

<section class="page page--right">
  <div class="band-top"></div>
  <div class="brand"><span class="brand__dot"></span><span class="brand__name">TAMBERLY GROUP</span></div>
  <h1 class="title">COMMERCIAL PROPERTIES WE INSPECT</h1>
  <div class="sky" role="img" aria-label="Pale sky with a glass office tower"></div>
  <div class="grid">
    <div class="tile"><svg><use href="#bldg"/></svg>Apartments</div>
    <div class="tile"><svg><use href="#bldg"/></svg>Strip Centers</div>
    <div class="tile"><svg><use href="#bldg"/></svg>Hotels/Motels</div>
    <div class="tile"><svg><use href="#bldg"/></svg>Churches</div>
    <div class="tile"><svg><use href="#bldg"/></svg>Retail</div>
    <div class="tile"><svg><use href="#bldg"/></svg>Leases</div>
    <div class="tile"><svg><use href="#bldg"/></svg>Hospitals</div>
    <div class="tile"><svg><use href="#bldg"/></svg>Day Cares</div>
    <div class="tile"><svg><use href="#bldg"/></svg>Multi-Family</div>
    <div class="tile"><svg><use href="#bldg"/></svg>Warehouses</div>
    <div class="tile"><svg><use href="#bldg"/></svg>Industrial</div>
    <div class="tile"><svg><use href="#bldg"/></svg>Restaurants</div>
  </div>
  <div class="band-bottom"></div>
  <div class="mark-faint"></div>
  <div class="inspector" role="img" aria-label="Inspector in work vest holding a report binder"></div>
  <p class="domain">QUORVATO.COM</p>
</section>
</body>
</html>
```